Tarwin Project Consulting

I need a logo and business card design for a small business operating in the management consulting and contractor space, predominantly in local and state government. I specialise in project management, financial consulting, people and culture, procurement, ICT transformation and contracting for corporate support areas of organisations.

Industry/Entity Type

Business

```html
<!DOCTYPE html>
<html lang="en">
<head>
<meta charset="utf-8">
<title>Tarwin Project Consulting – Business Cards</title>
<link href="https://fonts.googleapis.com/css2?family=Open+Sans:wght@400;600;700&display=swap" rel="stylesheet">
<style>
  :root {
    --brand-red: #f5162b;
    --brand-grey: #a7a9ac;
    --wordmark-grey: #a3a5a8;
    --card-white: #ffffff;
    --page-bg: #eeeae6;
    --text-light: #ffffff;
  }
  * { margin: 0; padding: 0; box-sizing: border-box; }
  html, body {
    width: 1200px; height: 900px; overflow: hidden;
    background: var(--page-bg);
    font-family: "Open Sans", Arial, sans-serif;
  }
  .canvas { position: relative; width: 1200px; height: 900px; }

  .card {
    position: absolute;
    background: var(--card-white);
    overflow: hidden;
    box-shadow: 0 6px 18px rgba(0,0,0,0.12);
  }
  .card--front { left: 237px; top: 55px; width: 593px; height: 365px; }
  .card--back  { left: 444px; top: 513px; width: 576px; height: 354px; }

  .brand { position: absolute; display: flex; align-items: center; gap: 22px; }
  .card--front .brand { left: 145px; top: 47px; }
  .card--back  .brand { left: 141px; top: 42px; }
  .brand__dot {
    width: 126px; height: 126px; border-radius: 50%;
    background: var(--brand-red); flex: none;
  }
  .brand__name {
    color: var(--wordmark-grey);
    font-weight: 600;
    font-size: 30px;
    line-height: 38px;
    text-transform: uppercase;
    letter-spacing: 2px;
  }

  .band { position: absolute; left: 0; right: 0; bottom: 0; color: var(--text-light); }
  .band--contact { top: 198px; background: var(--brand-red); }
  .band--services { top: 193px; background: var(--brand-grey); }

  .holder { position: absolute; right: 310px; top: 34px; text-align: right; }
  .holder__name { font-weight: 700; font-size: 21px; line-height: 28px; }
  .holder__role { font-size: 16px; line-height: 22px; }

  .contact-list { position: absolute; left: 309px; top: 25px; list-style: none; }
  .contact-list li {
    display: flex; align-items: center; gap: 9px;
    font-size: 16px; line-height: 21.5px;
  }
  .contact-list svg { width: 12px; height: 12px; fill: var(--text-light); flex: none; }

  .address { position: absolute; left: 112px; top: 109px; font-size: 16px; }

  .services__heading {
    position: absolute; left: 0; right: 0; top: 28px;
    display: flex; align-items: center; justify-content: center; gap: 16px;
    font-weight: 700; font-size: 18px; letter-spacing: 0.3px;
  }
  .services__heading::before, .services__heading::after {
    content: ""; height: 1px; width: 180px; background: rgba(255,255,255,0.85);
  }
  .services__list {
    position: absolute; left: 0; right: 0; top: 64px;
    text-align: center; font-size: 16px; line-height: 21px;
  }
</style>
</head>
<body>
<main class="canvas">

  <section class="card card--front" aria-label="Business card front">
    <div class="brand">
      <span class="brand__dot"></span>
      <p class="brand__name">Tarwin<br>Project<br>Consulting</p>
    </div>
    <div class="band band--contact">
      <div class="holder">
        <p class="holder__name">Daniel Hartley</p>
        <p class="holder__role">Managing Director</p>
      </div>
      <ul class="contact-list">
        <li>
          <svg viewBox="0 0 24 24" aria-hidden="true"><path d="M6.6 10.8a15.1 15.1 0 0 0 6.6 6.6l2.2-2.2a1 1 0 0 1 1-.25 11.4 11.4 0 0 0 3.6.57 1 1 0 0 1 1 1V20a1 1 0 0 1-1 1A17 17 0 0 1 3 4a1 1 0 0 1 1-1h3.5a1 1 0 0 1 1 1c0 1.25.2 2.45.57 3.57a1 1 0 0 1-.25 1z"/></svg>
          044-987 650 214
        </li>
        <li>
          <svg viewBox="0 0 24 24" aria-hidden="true"><path d="M2 5h20v14H2z M3 6l9 7 9-7" stroke="#f5162b" stroke-width="1.5"/></svg>
          info@tarwinpc.com
        </li>
        <li>
          <svg viewBox="0 0 24 24" aria-hidden="true"><circle cx="12" cy="12" r="11"/><path d="M1 12h22M12 1c-4 4-4 18 0 22M12 1c4 4 4 18 0 22" stroke="#f5162b" stroke-width="1.5" fill="none"/></svg>
          www.tarwinpc.com
        </li>
      </ul>
      <p class="address">48 Wattle Street, Ballarat VIC, Australia 3350.</p>
    </div>
  </section>

  <section class="card card--back" aria-label="Business card back">
    <div class="brand">
      <span class="brand__dot"></span>
      <p class="brand__name">Tarwin<br>Project<br>Consulting</p>
    </div>
    <div class="band band--services">
      <h2 class="services__heading">SPECIALISE IN</h2>
      <p class="services__list">
        Project management | Financial consulting | People and culture<br>
        Procurement | ICT transformation and<br>
        Contracting for corporate support areas of organisations.
      </p>
    </div>
  </section>

</main>
</body>
</html>
```